Web 2.0 my 1 page website ($500 Guaranteed)

Im looking for someone who can update my existing design at http://www.doriselvanby.com
I like existing layout and the way the boxes all work. Looking for the same design but with an updated web 2.0 textured look and feel.
Please note the current site is already working on top of pagecrate and new design needs to also work with pagecrate so I can continue to page content.
Looking for designer who can also get it working in pagecrate as it is today.
$500 AUD first prize for it all working.
If it helps:
I like minimailist. I like white. I like bright. I like texture. I like backgrounds. I like horizontal stripes running the length of the page. I like designs that work regardless of width of page. I like big bold statements. I like obvious. I like round edges. I like sites that look like they have come alive. I like depth. I like a 3D look. I like something very subtle that moves occassionally - just enough to catch your eye. I dont like popups. I dont like scrolling.
I like really clean SEO friendly source code. I like standards compatible design.
http://www.lotvessel.ie/ I like the depth of the mini coming out of the screen. I like the big bold fonts and the bright colours. I like the horizontal red stripe running the length of the page.
http://www.quillharbor.ie/ I like the backround clouds. I like the nice big lettering on the font on the mene bar. I like the nice bog boxes and contact numbers.
http://www.kuljepolkuja.fi/ I like the bright colours on the phone. I like the splash of the bubbles at the top of the page.
http://ontheruncue.me/ I like the blurred background. I REALLY like the rounded enter your email and notify me text boxes. I like the fonts on notify me and the textured background of the button.
http://9qtorn.com/it/ I really like the horizontal bar across the page - I like the big fonts in this background - I like the green and the orange. I really like the depth - how the beans and chair and butterfly sit on top of the page kind of bringing it to life. Like all the layers giving that illusion of 3D.
http://www.fenwrigley.net/ Like the big fonts, the horizontal bar, the leather stitching look around the "lets work together" and how everything is shadowed and sits off the page. I like the big contact us / get in touch / fonts at the bottom the big social media buttons. Probably this area could all be half the size but I like it.
http://www.drevoxis.com/ I like the graining textures in the background grays. I prefer blues and whites.
http://tibbinshedding.ca/ Like the big bold texts and the colours. Like the 3D cardboard box coming off the page.
http://pondchimers.com/ Like the textured backround - the rough grainy blue.
http://www.uk-rv.com/ I always liked those background kind of bursts behind the bay area picture in the middle. Like the striped blue background.
http://workshop.vendoqua.com/ Who doesnt like a ninja, but again like the big fonts and the way the person has depth
http://www.plumfolders.com/ I like the depth. I like the big bold colours.
http://www.5ibrelt.com/ Again like how the product is featured with lighting behind it, has that 3D look. Nice big lettering etc.
Updates
I like minimailist. I like white. I like bright. I like texture. I like
backgrounds. I like horizontal stripes running the length of the page. I
like designs that work regardless of width of page. I like big bold
statements. I like obvious. I like round edges. I like sites that look
like they have come alive. I like depth. I like a 3D look. I like
something very subtle that moves occassionally - just enough to catch
your eye. I dont like popups. I dont like scrolling.
http://www.lotvessel.ie/
I like the depth of the mini coming out of the screen. I like the big
bold fonts and the bright colours. I like the horizontal red stripe
running the length of the page.
http://www.quillharbor.ie/
I like the backround clouds. I like the nice big lettering on the font
on the mene bar. I like the nice bog boxes and contact numbers.
http://ontheruncue.me/
I like the blurred background. I REALLY like the rounded enter your
email and notify me text boxes. I like the fonts on notify me and the
textured background of the button.
http://9qtorn.com/it/
I really like the horizontal bar across the page - I like the big fonts
in this background - I like the green and the orange. I really like the
depth - how the beans and chair and butterfly sit on top of the page
kind of bringing it to life. Like all the layers giving that illusion of
3D.
http://www.fenwrigley.net/
Like the big fonts, the horizontal bar, the leather stitching look
around the "lets work together" and how everything is shadowed and sits
off the page. I like the big contact us / get in touch / fonts at the
bottom the big social media buttons. Probably this area could all be
half the size but I like it.
Typical Components of Web 2.0 Site Design
- Lots of space: Web 2.0 sites tend to have a lot of wide-open space. It's a contrast from the 90s, where the trend was to make usage of every square inch of a website's home page with links, banners and applets. White space is embraced to a major degree, as it calls attention to important buttons and links.
- The "Less Is More" Mentality: By putting less on the page, you're drawing more attention to the elements that matter: content and call-to-action buttons. "Clutter" and Web 2.0 simply do not mix - this is a new era of design psychology.
- Gradients: Merely a design element, gradients are used in Web 2.0 site design to give a clean, soft impression that's easy on the eyes.
- Large Fonts: Huge headings are a popular trend in Web 2.0 design - headings are usually taglines that describe or summarize what a website is about in just a handful of words. It's a huge benefit to first-timer usability, especially since new visitors would like to "get to the point" without having to read an intro paragraph.
- Dramatic Color Contrast: Another typical element seen in Web 2.0 design are bright colors (particularly neon colors) that accent site elements including menus, separator bars and footers. Many sites use this same neon color for their hyperlinks and headings, as well. Sometimes, the contrast between bright neon colors and charcoal or light gray text are put in unison for a dramatic effect.
- Eye Candy Logos: In Web 2.0 logo design, it's almost expected to see logos have a shiny plastic luster, or a soft gradient. Most Web 2.0 fonts are similar to basic Arial, Tahoma or Helvetica, and are simple. The colors used within the logo are also typically mimicked on other site design pieces to create a sense of uniformity.
- Huge Buttons: Calls to action (buttons that prompt you to "Get More Information," "Download Now," "See A Demo" or "Buy Now") are typically gigantic in Web 2.0 design. They're also attractive, featuring a color that strays away from the rest of the website's schematic. These buttons are typically isolated by a great deal of space, making them very easy to notice.
- Reflections: Product images, screenshots and icons can be seen as having "reflections" underneath them, as if they were standing on top of a new laminate floor. It's a stereotypical design element of Web 2.0.
- Lots of Icons: Web 2.0 icons are always in vector format, which is the standard format created by software such as Adobe Illustrator and Flash. They're attractive and clean looking, and are used to either draw attention to a website's sub-categories, a product's individual features, or anything else that the web designer wanted to help associate for a viewer.
- Exaggerated Web Form Fields: Huge form fields add to usability and draw attention to sign-ups and registrations. Instead of typing in a search, a username or anything else into a tiny web field, Web 2.0 has evolved them into massive interactive boxes with large text that makes things easy to see. For a good example, look at Glimvo.com's huge fields.

```html
<!DOCTYPE html>
<html lang="en">
<head>
<meta charset="utf-8">
<title>Doris Elvanby — Retail CIO</title>
<link href="https://fonts.googleapis.com/css2?family=Ubuntu:wght@400;500;700&family=Open+Sans:ital,wght@1,700&display=swap" rel="stylesheet">
<style>
:root{
  --bar:#232e38;
  --sky-top:#3d9fdd;
  --sky-mid:#8fd0e2;
  --sky-low:#b5e0e2;
  --ground:#d9dbdc;
  --name-dark:#2c5a73;
  --ink:#2a2a2a;
  --muted:#555c62;
  --link:#2a6fa8;
  --accent:#2a6496;
  --panel:rgba(244,249,252,.86);
  --panel-back:rgba(236,244,250,.55);
  --panel-line:rgba(90,140,175,.55);
  --card:#f5f9fc;
  --portrait-top:#26323b;
  --portrait-low:#0c1318;
}
*{margin:0;padding:0;box-sizing:border-box}
html,body{width:1200px;height:900px;overflow:hidden}
body{position:relative;font-family:Arial,Helvetica,sans-serif;
  background:linear-gradient(180deg,var(--sky-top) 0,#5fb6e2 260px,var(--sky-mid) 420px,var(--sky-low) 560px,#cfe0e0 620px,var(--ground) 720px,#e2e3e3 880px);}
.top-band,.bottom-band{position:absolute;left:0;width:1200px;background:var(--bar)}
.top-band{top:0;height:19px}
.bottom-band{top:882px;height:18px}
.grid{position:absolute;left:0;top:19px;width:1200px;height:620px;
  background-image:linear-gradient(90deg,rgba(255,255,255,.28) 1px,transparent 1px),linear-gradient(0deg,rgba(255,255,255,.22) 1px,transparent 1px);
  background-size:96px 96px;background-position:20px 0,0 -1px;
  -webkit-mask-image:linear-gradient(180deg,#000 70%,transparent);mask-image:linear-gradient(180deg,#000 70%,transparent)}
.brand{position:absolute;left:146px;top:48px}
.brand-name{font-family:Ubuntu,sans-serif;font-weight:700;font-size:31px;line-height:30px;letter-spacing:.5px;text-transform:uppercase}
.brand-name .first{color:var(--name-dark);display:block}
.brand-name .last{color:#f4f9fc;display:block;text-shadow:0 1px 2px rgba(0,0,0,.35)}
.brand-role{font-size:19px;color:#333;margin-top:10px}
.panel{position:absolute;border:1px solid var(--panel-line);overflow:hidden}
.panel-back{background:var(--panel-back);height:110px;top:104px;width:306px}
.panel-mid{background:var(--panel);top:154px;height:228px;width:362px;box-shadow:0 2px 6px rgba(0,0,0,.12)}
.panel h2{font-family:"Open Sans",sans-serif;font-style:italic;font-weight:700;display:flex;align-items:center;gap:8px}
.panel-back h2{font-size:16px;color:#4b6f88;padding:10px 0 0 10px}
.panel-mid h2{font-size:19px;color:#3a3a3a;padding:14px 0 0 20px}
.panel p{font-size:9.5px;font-style:italic;color:var(--muted);line-height:12.3px}
.panel-back p{padding:4px 10px 0 18px;opacity:.6}
.panel-mid p{padding:8px 18px 0 20px}
.dot{width:30px;height:30px;border-radius:50%;background:#4b6f88;display:inline-block}
.welcome{position:absolute;left:445px;top:207px;width:529px;height:333px;background:var(--card);
  border-top:2px solid #1c4a70;border-radius:2px;box-shadow:0 6px 14px rgba(0,0,0,.22);padding:22px 34px 0 32px}
.welcome h1{font-family:"Open Sans",sans-serif;font-style:italic;font-weight:700;font-size:27px;color:#333;display:flex;align-items:center;gap:10px}
.welcome p{font-size:13px;font-style:italic;color:var(--ink);line-height:18.1px;margin-top:18px;letter-spacing:.3px}
.welcome p+p{margin-top:0}
a{color:var(--link);text-decoration:none}
.portrait{position:absolute;left:90px;top:258px;width:325px;height:334px;border-radius:6px;
  background:linear-gradient(180deg,var(--portrait-top),var(--portrait-low));
  box-shadow:0 0 18px rgba(255,255,255,.35)}
.statement-frame{position:absolute;left:147px;top:605px;width:908px;height:170px;border-radius:4px;
  background:rgba(200,210,212,.45);border:1px solid rgba(170,180,182,.6)}
.statement-frame::before{content:"";position:absolute;left:43px;top:4px;border:10px solid transparent;border-bottom-color:#f2f2f2;border-top:0}
.statement{position:absolute;left:18px;top:17px;width:870px;height:136px;border-radius:4px;
  background:linear-gradient(180deg,#f4f4f4,#dcdcdc);box-shadow:0 1px 3px rgba(0,0,0,.25);padding:16px 20px}
.statement p{font-family:Ubuntu,sans-serif;font-weight:500;font-size:26px;line-height:31.5px;color:#222;letter-spacing:-.3px}
.statement .role{color:var(--accent)}
.social{position:absolute;right:12px;bottom:8px;display:flex;align-items:center;gap:6px}
.social .label{font-size:12px;color:#222;margin-right:8px}
.social a{width:30px;height:30px;border-radius:50%;display:block;position:relative}
.social .chirp{background:#3c9fcf}
.social .link{background:#4a4a4a}
.sr{position:absolute;width:1px;height:1px;overflow:hidden;clip:rect(0 0 0 0)}
.copyright{position:absolute;left:172px;top:781px;font-size:12px;color:#222}
</style>
</head>
<body>
<div class="top-band"></div>
<div class="grid"></div>

<header class="brand">
  <div class="brand-name"><span class="first">Doris</span><span class="last">Elvanby</span></div>
  <div class="brand-role">Retail CIO</div>
</header>

<section class="panel panel-back" style="left:397px">
  <h2><span class="dot"></span>Tweets</h2>
  <p>Lorem ipsum dolor sit amet, consectetuer adipiscing elit. Aenean commodo ligula eget dolor. Aenean massa. Cum sociis natoque penatibus et magnis dis parturient montes nascetur.</p>
</section>
<section class="panel panel-back" style="left:706px">
  <h2><svg width="32" height="32" viewBox="0 0 32 32" fill="none" stroke="#4b6f88" stroke-width="4"><path d="M5 16a11 11 0 0 1 19-7.5"/><path d="M27 16a11 11 0 0 1-19 7.5"/><path d="M25 3v7h-7M7 29v-7h7" stroke-width="3"/></svg>Current Interests</h2>
  <p>Lorem ipsum dolor sit amet, consectetuer adipiscing elit. Aenean commodo ligula eget dolor. Aenean massa. Cum sociis natoque penatibus et magnis dis parturient montes nascetur.</p>
</section>

<section class="panel panel-mid" style="left:332px">
  <h2><svg width="30" height="26" viewBox="0 0 30 26"><rect x="10" y="1" width="10" height="6" rx="2" fill="none" stroke="#4a4f55" stroke-width="2.4"/><rect x="0" y="5" width="30" height="21" rx="3" fill="#4a4f55"/><rect x="0" y="12" width="30" height="2" fill="#f4f9fc"/><rect x="12" y="10" width="6" height="6" rx="1" fill="#f4f9fc"/></svg>Career Timeline</h2>
  <p>Lorem ipsum dolor sit amet, consectetuer adipiscing elit. Aenean commodo ligula eget dolor. Aenean massa. Cum sociis natoque penatibus et magnis dis parturient montes, nascetur ridiculus mus. Donec quam felis, ultricies nec, pellentesque eu, pretium quis, sem. Nulla consequat massa quis enim. Donec pede justo, fringilla vel, aliquet nec, vulputate eget, arcu. In enim justo, rhoncus ut, imperdiet a, venenatis vitae, justo. Nullam dictum felis eu pede mollis pretium. Integer tincidunt. Cras dapibus. Vivamus elementum semper nisi. Aenean vulputate eleifend tellus. Aenean leo ligula, porttitor eu, consequat vitae, eleifend ac, enim. Aliquam lorem ante, dapibus in, viverra quis, feugiat a, tellus. Phasellus viverra nulla ut metus varius laoreet. Etiam ultricies nisi vel augue.</p>
</section>
<section class="panel panel-mid" style="left:714px">
  <h2><svg width="32" height="32" viewBox="0 0 32 32"><path d="M29 3c-2-2-5 0-7 2l-4 4-13-3-3 3 10 6-5 5-4-1-2 2 5 3 3 5 2-2-1-4 5-5 6 10 3-3-3-13 4-4c2-2 4-5 2-7z" fill="#4a4f55"/></svg>Travelling Australia</h2>
  <p>Lorem ipsum dolor sit amet, consectetuer adipiscing elit. Aenean commodo ligula eget dolor. Aenean massa. Cum sociis natoque penatibus et magnis dis parturient montes, nascetur ridiculus mus. Donec quam felis, ultricies nec, pellentesque eu, pretium quis, sem. Nulla consequat massa quis enim. Donec pede justo, fringilla vel, aliquet nec, vulputate eget, arcu. In enim justo, rhoncus ut, imperdiet a, venenatis vitae, justo. Nullam dictum felis eu pede mollis pretium. Integer tincidunt. Cras dapibus. Vivamus elementum semper nisi. Aenean vulputate eleifend tellus. Aenean leo ligula, porttitor eu, consequat vitae, eleifend ac, enim. Aliquam lorem ante, dapibus in, viverra quis, feugiat a, tellus. Phasellus viverra nulla ut metus varius laoreet. Quisque rutrum. Aenean imperdiet.</p>
</section>

<div class="portrait" role="img" aria-label="Portrait photo of Doris Elvanby"></div>

<main class="welcome">
  <h1><svg width="42" height="40" viewBox="0 0 42 40"><rect x="0" y="6" width="42" height="34" rx="4" fill="#4a4f55"/><rect x="15" y="0" width="12" height="10" rx="3" fill="#4a4f55" stroke="#f5f9fc" stroke-width="2"/><circle cx="12" cy="21" r="5" fill="#f5f9fc"/><path d="M4 34c1-6 4-8 8-8s7 2 8 8z" fill="#f5f9fc"/><rect x="23" y="18" width="14" height="3" fill="#f5f9fc"/><rect x="23" y="25" width="14" height="3" fill="#f5f9fc"/></svg>Welcome</h1>
  <p>Lorem ipsum dolor sit amet, consectetuer adipiscing elit. Aenean commodo ligula eget dolor. Aenean massa. Cum sociis natoque penatibus et magnis dis parturient montes, nascetur ridiculus mus. Donec quam felis, ultricies nec, pellentesque eu, <a href="#">pretium quis</a>, sem. Nulla consequat massa quis enim. Donec pede justo, fringilla vel, aliquet nec, vulputate eget, arcu. In enim justo, rhoncus ut, imperdiet a, venenatis vitae, justo. Nullam dictum felis eu pede mollis pretium. Integer tincidunt.</p>
  <p>Cras dapibus. Vivamus elementum semper nisi. Aenean vulputate eleifend tellus. Aenean leo ligula, porttitor eu, <a href="#">consequat vitae</a>, eleifend ac, enim. Aliquam lorem ante, dapibus in, viverra quis, feugiat a, tellus. Phasellus viverra nulla ut metus varius laoreet. Quisque rutrum. Aenean imperdiet. Etiam ultricies nisi vel augue.</p>
</main>

<section class="statement-frame">
  <div class="statement">
    <p><span class="role">Retail CIO</span> with a passion for multichannel, multi-store technology.<br>Specialize in using online communities to hlep drive the business<br>by consumer engagement</p>
    <div class="social">
      <span class="label">Find me at</span>
      <a class="chirp" href="#"><span class="sr">Chirpline</span></a>
      <a class="link" href="#"><span class="sr">Linkwell</span></a>
    </div>
  </div>
</section>

<footer class="copyright">Copyriht @ 2011 Doris Elvanby</footer>
<div class="bottom-band"></div>
</body>
</html>
```